Modern Billboard Ad for Criminal Defense Firm

10.5 x 36 We're looking for something to set us apart from the local competition. Looking for sleek and modern. We're a mid-sized firm in a small market city. We want to give the artist room to be creative on this one.
Thanks

Target Market(s)

Adult clients who have been charged with a crime/DWI

Industry/Entity Type

legal

Font styles to use
Serif
Sans Serif

Requirements
Must have
• Needs to have the firm name in large lettering. Law Offices of Marcus T Whitfield. “PLLC” does not have to be included. Phone number of (555) 384-1927 should be included but not the main focus.
Nice to have
• A call to action or something similar. “Don’t go it alone, call today.”, “ Arrested?”

```html
<!DOCTYPE html>
<html lang="en">
<head>
<meta charset="utf-8">
<title>Arrested? Don't go it alone – Law Offices of Marcus T Whitfield</title>
<link href="https://fonts.googleapis.com/css2?family=Anton&family=Barlow+Semi+Condensed:wght@600&family=Montserrat:wght@500;700&family=Poppins:wght@600&display=swap" rel="stylesheet">
<style>
  :root {
    --page: #ffffff;
    --beige: #dedbd0;
    --slate: #627b93;
    --skin-light: #f0d2c2;
    --skin-dark: #d9a891;
    --stamp-red: #e8141b;
    --ink: #57524c;
    --white: #ffffff;
    --badge-dark: #1f1f22;
    --badge-blue: #1aa3e0;
  }
  * { margin: 0; padding: 0; box-sizing: border-box; }
  html, body { width: 1200px; height: 848px; overflow: hidden; background: var(--page); }
  .canvas { position: relative; width: 1200px; height: 848px; }

  .billboard {
    position: absolute; left: 113px; top: 278px;
    width: 952px; height: 277px; overflow: hidden;
    background: var(--white);
  }
  .billboard__shapes { position: absolute; left: 0; top: 0; }

  .hands-photo {
    position: absolute; left: 232px; top: 0; width: 258px; height: 198px;
    background: linear-gradient(180deg, var(--skin-light) 0%, var(--skin-dark) 100%);
    border-radius: 0 0 50px 50px;
    opacity: .8;
  }

  .stamp {
    position: absolute; left: 488px; top: 20px; width: 366px; height: 108px;
    border: 6px solid var(--stamp-red); border-radius: 10px;
    transform: rotate(-4deg);
    display: flex; align-items: center; justify-content: center;
  }
  .stamp__word {
    font-family: "Anton", sans-serif; font-size: 80px; line-height: 1;
    color: var(--stamp-red); letter-spacing: 1px;
  }
  .stamp-question {
    position: absolute; left: 858px; top: 6px;
    font-family: "Anton", sans-serif; font-size: 98px; line-height: 1;
    color: var(--stamp-red);
  }

  .tagline {
    position: absolute; right: 26px; top: 137px;
    font-family: "Montserrat", sans-serif; font-weight: 700;
    font-size: 21px; line-height: 1; letter-spacing: 2px; color: var(--ink);
  }

  .firm { position: absolute; left: 267px; top: 206px; color: var(--white); }
  .firm__prefix {
    font-family: "Montserrat", sans-serif; font-weight: 500;
    font-size: 17px; letter-spacing: 5px; line-height: 1;
  }
  .firm__name {
    font-family: "Barlow Semi Condensed", sans-serif; font-weight: 600;
    font-size: 41px; line-height: 1; margin-top: 4px; letter-spacing: .3px;
  }

  .divider {
    position: absolute; left: 654px; top: 225px; width: 3px; height: 41px;
    background: var(--white);
  }

  .contact { position: absolute; left: 671px; top: 223px; color: var(--white); }
  .contact__label {
    font-family: "Montserrat", sans-serif; font-weight: 700;
    font-size: 13px; letter-spacing: 4.5px; line-height: 1;
  }
  .contact__phone {
    font-family: "Poppins", sans-serif; font-weight: 600;
    font-size: 24px; line-height: 1; margin-top: 5px; letter-spacing: .3px;
  }

  .award-badge {
    position: absolute; left: 893px; top: 197px; width: 51px; height: 75px;
    background: var(--badge-dark);
    border: 2px solid var(--badge-blue);
  }
</style>
</head>
<body>
<main class="canvas">
  <section class="billboard">
    <svg class="billboard__shapes" viewBox="0 0 952 277" width="952" height="277" aria-hidden="true">
      <path d="M293 0 L952 0 L952 161 C880 176 800 184 708 182 C620 180 560 160 503 133 C420 92 340 40 293 0 Z" fill="#dedbd0"/>
      <path d="M256 153 C330 180 420 204 503 207 C580 212 650 213 708 210 C800 204 880 192 952 176 L952 277 L150 277 Z" fill="#627b93"/>
    </svg>

    <svg class="portrait" style="position:absolute;left:0;top:0" width="270" height="277" viewBox="0 0 270 277" role="img" aria-label="Black-and-white portrait of the attorney in a vest and tie, jacket over his shoulder">
      <defs>
        <linearGradient id="portraitTone" x1="0" y1="0" x2="1" y2="1">
          <stop offset="0" stop-color="#a9b8c6"/>
          <stop offset="1" stop-color="#4e6377"/>
        </linearGradient>
      </defs>
      <path d="M0 0 L154 0 C215 25 262 110 258 180 C254 230 215 265 170 277 L0 277 Z" fill="url(#portraitTone)"/>
    </svg>

    <div class="hands-photo" role="img" aria-label="Photo of two clenched hands locked in steel handcuffs"></div>

    <div class="stamp"><span class="stamp__word">ARRESTED</span></div>
    <span class="stamp-question">?</span>

    <p class="tagline">DON’T GO IT ALONE.</p>

    <div class="firm">
      <p class="firm__prefix">LAW OFFICES OF</p>
      <h1 class="firm__name">MARCUS T WHITFIELD</h1>
    </div>

    <div class="divider"></div>

    <div class="contact">
      <p class="contact__label">CALL TODAY</p>
      <p class="contact__phone">(555) 384-1927</p>
    </div>

    <div class="award-badge" role="img" aria-label="Community award badge"></div>
  </section>
</main>
</body>
</html>
```